Proposal & Presentation Slides

We need power point slides template to build proposal for prospects. slides should include: We provide prospect two items, presentation and proposal. We need power point slide design that can be used for both. One of the following option will work:
So we can include 1-2 slides in proposal to demonstrate service included
or
we can use power power slides and last 1-2 slides will have page for them to sign off.

Target Market(s)

It varies: we are IT Management Firm and provide servies to many different companies in Canada

Industry/Entity Type

Business Consultant

Font styles to use
Serif

Colors

Designer to choose colors to be used in the design.

Requirements
Must have
• Information about our company
• About Tidewell Process
• Proposal sign off form
• Colors : we had logo design project on sketchmarket, please use all logos and colors accordingly

```html
<!DOCTYPE html>
<html lang="en">
<head>
<meta charset="utf-8">
<title>Tidewell Proposal Slides</title>
<link rel="stylesheet" href="https://fonts.googleapis.com/css2?family=Montserrat:ital,wght@0,400;0,500;0,600;0,700;0,800;1,800&display=swap">
<style>
:root{
  --red:#c8102e;
  --red-deep:#a9252b;
  --red-dark:#a0151f;
  --ink:#333333;
  --grey:#7f7f7f;
  --row:#dcdcdc;
  --white:#ffffff;
  --stage:#000000;
}
*{box-sizing:border-box;margin:0;padding:0}
html,body{width:1200px;height:699px;overflow:hidden;background:var(--stage)}
body{position:relative;font-family:'Montserrat',sans-serif;color:var(--ink)}
.slide{position:absolute;width:565px;height:319px;background:var(--white);overflow:hidden}
.slide--cost{left:18px;top:13px}
.slide--req{left:614px;top:13px}
.slide--divider{left:16px;top:360px;height:317px}
.slide--icons{left:613px;top:358px;height:318px}
.accent{position:absolute;left:0;top:21px;width:4px;height:34px;background:var(--red)}
.title{position:absolute;left:14px;top:27px;font-size:20px;font-weight:800;letter-spacing:.2px;color:var(--red)}
.title .dark{color:var(--ink)}
.brand{position:absolute;right:16px;top:19px;display:flex;align-items:center;gap:4px;font-size:15px;font-weight:600;color:var(--red);letter-spacing:.5px}
.brand .dot{width:7px;height:7px;border-radius:50%;background:var(--red)}
.footer{position:absolute;left:0;bottom:0;width:100%;height:25px;background:var(--red-deep);color:var(--white);font-size:12.5px;font-weight:800;font-style:italic;letter-spacing:.6px;text-align:center;line-height:25px}
.cost-table{position:absolute;left:29px;top:68px;width:525px;border-collapse:separate;border-spacing:0 2px;box-shadow:0 0 4px rgba(0,0,0,.25);background:var(--white);font-size:11.5px}
.cost-table th{background:var(--red-deep);color:var(--white);font-weight:600;font-size:14px;height:32px;letter-spacing:.5px}
.cost-table td{background:var(--row);height:31px;text-align:center;color:#444}
.subtitle{position:absolute;left:14px;top:58px;font-size:9.5px;color:#444}
.pie{position:absolute;left:158px;top:60px}
.pie text{font-family:'Montserrat',sans-serif;font-size:11.5px;font-weight:500;fill:var(--white)}
.legend{position:absolute;left:472px;top:204px;width:86px;height:73px;background:#f2f2f2;padding:13px 0 0 10px;font-size:10px;color:#555;line-height:17px}
.legend li{list-style:none;display:flex;align-items:center;gap:4px}
.legend i{width:5px;height:5px;display:inline-block}
.divider-bg{position:absolute;inset:0;background:radial-gradient(circle at 62% 50%,#c53a3e 0%,#a8222a 50%,#8e161d 100%)}
.divider-brand{position:absolute;left:48px;top:148px;display:flex;align-items:center;gap:6px;color:var(--white);font-size:29px;font-weight:500;letter-spacing:1px}
.divider-brand .dot{width:12px;height:12px;border-radius:50%;background:var(--white)}
.divider-rule{position:absolute;left:242px;top:139px;width:1px;height:66px;background:var(--white)}
.divider-title{position:absolute;left:256px;top:146px;color:var(--white);font-size:21.5px;font-weight:800;letter-spacing:.3px}
.divider-text{position:absolute;left:258px;top:177px;width:270px;color:var(--white);font-size:8.5px;line-height:14px}
.icons-bar{position:absolute;left:28px;top:0;width:8px;height:38px;background:var(--red-dark)}
.icons-title{position:absolute;left:43px;top:16px;font-size:17.5px;font-weight:800;color:var(--red)}
.icons-sub{position:absolute;left:44px;top:37px;font-size:10px;color:#555}
.slide--icons .brand{top:20px;right:18px}
.feature{position:absolute;top:85px;width:135px;text-align:center}
.feature svg{display:block;margin:0 auto;height:44px}
.feature h3{margin-top:17px;font-size:12px;font-weight:600;color:var(--red);letter-spacing:.2px}
.feature p{margin-top:6px;font-size:7px;line-height:12.2px;color:#444;text-align:justify}
.f1{left:51px}.f2{left:225px}.f3{left:386px}
.icons-base{position:absolute;left:0;bottom:0;width:100%;height:8px;background:var(--red)}
.page-no{position:absolute;left:522px;bottom:-4px;width:26px;height:26px;border-radius:50%;background:var(--red-dark);border:2px solid var(--white);color:var(--white);font-size:7.5px;text-align:center;line-height:18px}
</style>
</head>
<body>

<section class="slide slide--cost">
  <div class="accent"></div>
  <h1 class="title">TOTAL TECHNOLOGY <span class="dark">COST</span></h1>
  <div class="brand"><span class="dot"></span>TIDEWELL</div>
  <table class="cost-table">
    <thead><tr><th>HARD COST</th><th>SOFT COST</th></tr></thead>
    <tbody>
      <tr><td>Direct Employees</td><td>Capital Costs</td></tr>
      <tr><td>Employee IT Training</td><td>Employee Productivity</td></tr>
      <tr><td>Employee Management (HR)</td><td>Business Risk(s)</td></tr>
      <tr><td></td><td></td></tr>
      <tr><td></td><td></td></tr>
    </tbody>
  </table>
  <div class="footer">LEADING YOUR BUSINESS IN THE RIGHT DIRECTION</div>
</section>

<section class="slide slide--req">
  <div class="accent"></div>
  <h1 class="title">BUSINESS REQUIREMENTS - <span class="dark">IT</span></h1>
  <div class="brand"><span class="dot"></span>TIDEWELL</div>
  <p class="subtitle">Business Requirements from IT Department</p>
  <svg class="pie" width="230" height="230" viewBox="-115 -115 230 230" role="img" aria-label="Pie chart of IT requirements">
    <path d="M0 0 L0 -114 A114 114 0 0 1 100.6 53.5 Z" fill="#cc0000" stroke="#fff" stroke-width="1.5"/>
    <path d="M0 0 L100.6 53.5 A114 114 0 0 1 -98.7 57 Z" fill="#a0151f" stroke="#fff" stroke-width="1.5"/>
    <path d="M0 0 L-98.7 57 A114 114 0 0 1 0 -114 Z" fill="#7f7f7f" stroke="#fff" stroke-width="1.5"/>
    <text x="53" y="-35" text-anchor="middle">Category</text><text x="53" y="-20" text-anchor="middle">Name here</text>
    <text x="-56" y="-35" text-anchor="middle">Category</text><text x="-56" y="-20" text-anchor="middle">Name here</text>
    <text x="0" y="51" text-anchor="middle">Category</text><text x="0" y="66" text-anchor="middle">Name here</text>
  </svg>
  <ul class="legend">
    <li><i style="background:#cc0000"></i>Infrastructure</li>
    <li><i style="background:#a0151f"></i>Support</li>
    <li><i style="background:#7f7f7f"></i>Strategy</li>
  </ul>
  <div class="footer">LEADING YOUR BUSINESS IN THE RIGHT DIRECTION</div>
</section>

<section class="slide slide--divider">
  <div class="divider-bg" role="img" aria-label="Red-toned globe with network lines"></div>
  <div class="divider-brand"><span class="dot"></span>TIDEWELL</div>
  <div class="divider-rule"></div>
  <h2 class="divider-title">SECTION DEVIDER HERE</h2>
  <p class="divider-text">Lorem Ipsum is simply dummy text of the printing and type-setting industry. Lorem Ipsum has been</p>
</section>

<section class="slide slide--icons">
  <div class="icons-bar"></div>
  <h1 class="icons-title">ICON COLOUMN</h1>
  <p class="icons-sub">Sub Heading text Here</p>
  <div class="brand"><span class="dot"></span>TIDEWELL</div>

  <div class="feature f1">
    <svg viewBox="0 0 44 44" fill="none" stroke="#c8102e" stroke-width="1.8"><rect x="1" y="2" width="42" height="40" rx="2"/><line x1="1" y1="10" x2="43" y2="10"/><circle cx="6" cy="6" r="1.3"/><circle cx="10" cy="6" r="1.3"/><circle cx="14" cy="6" r="1.3"/><line x1="6" y1="17" x2="30" y2="17"/><line x1="6" y1="24" x2="30" y2="24"/><line x1="6" y1="31" x2="30" y2="31"/><rect x="34" y="14" width="5" height="24"/></svg>
    <h3>ICONS TITLE HERE</h3>
    <p>Lorem Ipsum is simply dummy text of the printing and typesetting industry. Lorem Ipsum has been the industry's standard dummy text ever since the 1500s, when an unknown printer took a galley of type and scrambled it to make a type specimen book. It has survived not only five centuries, but also the leap into electronic typeset-ting, remaining essentially</p>
  </div>
  <div class="feature f2">
    <svg viewBox="0 0 44 48" fill="none" stroke="#2b2f6b" stroke-width="1.8"><path d="M12 20 V12 a10 10 0 0 1 20 0 V20"/><path d="M16 20 V12 a6 6 0 0 1 12 0 V20"/><circle cx="22" cy="32" r="14"/><circle cx="22" cy="32" r="9"/><path d="M20 28 a2 2 0 1 1 4 0 l-1 5 h-2 z"/></svg>
    <h3>ICONS TITLE HERE</h3>
    <p>Lorem Ipsum is simply dummy text of the printing and typesetting industry. Lorem Ipsum has been the industry's standard dummy text ever since the 1500s, when an unknown printer took a galley of type and scrambled it to make a type specimen book. It has survived not only five centuries, but also the leap into electronic typeset-ting, remaining essentially</p>
  </div>
  <div class="feature f3">
    <svg viewBox="0 0 48 44" fill="none" stroke="#2b2f6b" stroke-width="1.8"><rect x="2" y="2" width="44" height="26"/><line x1="0" y1="28" x2="48" y2="28" stroke="#c8102e"/><polyline points="7,22 15,14 21,18 29,9 35,14 41,8" stroke="#c8102e"/><line x1="24" y1="28" x2="24" y2="34"/><line x1="24" y1="34" x2="14" y2="43"/><line x1="24" y1="34" x2="34" y2="43"/><line x1="24" y1="34" x2="24" y2="43"/></svg>
    <h3>ICONS TITLE HERE</h3>
    <p>Lorem Ipsum is simply dummy text of the printing and typesetting industry. Lorem Ipsum has been the industry's standard dummy text ever since the 1500s, when an unknown printer took a galley of type and scrambled it to make a type specimen book. It has survived not only five centuries, but also the leap into electronic typeset-ting, remaining essentially</p>
  </div>

  <div class="icons-base"></div>
  <div class="page-no">01</div>
</section>

</body>
</html>
```